Baby Care Print Log for Nannies and Parents- Creating a brand/style I can use across different forms

I am creating a notebook for babysitters to use to communicate with parents about the children they care for. I will be creating many different forms (emergency contacts, daily logs, shopping lists, etc.)
I need a look and feel from which to style these forms from. I am starting by designing the daily baby care log. I need a designer to take my Word doc with just text on it, and create a visual approach to make this visually appealing.
I do not want this to be extremely "babyish" with cartoon styling. I want it to be more of a professional looking style. I would like to be able to color each different document a different color palette, yet keep the similar look and feel. My logo is attached for inspiration. I use real photography across my website plumhollowkit.com.
Updates
I will be re-designing my Wordpress website based on what design I like best and also will need other forms completed once I pick a design. I am hoping to work with someone who I can hire for further development needs as well. Added Saturday, February 11, 2017
Target Market(s)
Professional Parents
Industry/Entity Type
Education
Requirements
Must have
- color, pop, visual appeal
- Please use the color in my logo and any complementary colors that you think work well with it. I definitely like colored patterns, ombre, colored backgrounds, etc. I'd prefer for it not to be completely white with only pops of color here and there.
Nice to have
- My logo somewhere subtly on the form
- Photography elements
Should not have
- cartoon images of babies, etc. I use real photography across my website with the exception of my logo umbrella.

```html
<!DOCTYPE html>
<html lang="en">
<head>
<meta charset="utf-8">
<title>Plum Hollow Kit – Daily Care Log</title>
<link href="https://fonts.googleapis.com/css2?family=Carlito:wght@400;700&display=swap" rel="stylesheet">
<style>
  :root {
    --ink: #1e1e1e;
    --page-top: #e4f5fb;
    --page-mid: #fbf4ea;
    --page-bottom: #fbe6f1;
    --brand-sky: #3fb4dc;
    --nap-orange: #e98f2c;
    --feed-blue: #2f84da;
    --supply-pink: #e434b9;
    --crib-gold: #dcb25e;
    --bowl-teal: #3fc2de;
    --stroller-rose: #f08a94;
    --tub-gold: #e2b462;
    --blocks-mint: #6fd6a6;
    --bottle-brown: #6a3b26;
    --diaper-green: #7fe07a;
    --rule: #2a2a2a;
  }
  * { box-sizing: border-box; margin: 0; padding: 0; }
  html, body { width: 1200px; height: 1200px; overflow: hidden; }
  body {
    background: linear-gradient(180deg, var(--page-top) 0%, var(--page-mid) 55%, var(--page-bottom) 100%);
    font-family: "Carlito", "Calibri", sans-serif;
    color: var(--ink);
    font-size: 19px;
    line-height: 1.2;
    position: relative;
  }
  .form-title {
    position: absolute; top: 44px; left: 0; width: 100%;
    text-align: center; font-size: 46px; font-weight: 400;
    color: var(--brand-sky);
  }
  .col { position: absolute; width: 480px; }
  .col-left { left: 110px; }
  .col-right { left: 620px; }
  .label { font-weight: 700; }
  .nap { color: var(--nap-orange); }
  .feeding { color: var(--feed-blue); }
  .supplies { color: var(--supply-pink); }
  .icon { display: block; border-radius: 10px; }
  .log-head { display: flex; gap: 22px; }
  .log-row { display: flex; gap: 14px; margin-top: 20px; }
  .blank { display: inline-block; height: 20px; border-bottom: 1.5px solid var(--rule); }
  .icon-row { position: absolute; top: 700px; left: 110px; display: flex; gap: 60px; align-items: end; }
  .supply-list { display: grid; grid-template-columns: 270px 260px 200px; row-gap: 6px; margin-top: 16px; }
  .supply-list span.bullet::before { content: "○"; font-size: 13px; margin-right: 16px; position: relative; top: -2px; }
  .note-line { width: 980px; border-bottom: 1.5px solid var(--rule); height: 28px; }
</style>
</head>
<body>
  <h1 class="form-title">Plum Hollow Kit</h1>

  <div class="col col-left" style="top:150px"><span class="label">Name</span></div>
  <div class="col col-right" style="top:150px"><span class="label">Date</span></div>

  <div class="col col-left" style="top:215px"><span class="label nap">Nap Time</span>:</div>
  <div class="col col-right" style="top:215px"><span class="label feeding">Feeding</span></div>

  <div class="col col-left" style="top:255px">
    <div class="icon" role="img" aria-label="Gold crib with star mobile illustration" style="width:86px;height:86px;background:var(--crib-gold)"></div>
  </div>
  <div class="col col-right" style="top:275px">
    <div class="icon" role="img" aria-label="Teal bowl and spoon illustration" style="width:60px;height:66px;background:var(--bowl-teal)"></div>
  </div>

  <section class="col col-left" style="top:390px">
    <div class="log-head"><span>Time</span><span>How Long</span></div>
    <div class="log-row"><span class="blank" style="width:46px"></span><span class="blank" style="width:160px"></span></div>
    <div class="log-row"><span class="blank" style="width:46px"></span><span class="blank" style="width:160px"></span></div>
    <div class="log-row"><span class="blank" style="width:46px"></span><span class="blank" style="width:170px"></span></div>
    <div class="log-row"><span class="blank" style="width:46px"></span><span class="blank" style="width:170px"></span></div>
  </section>

  <section class="col col-right" style="top:390px">
    <div class="log-head"><span>Time</span><span>Milk (Type)</span><span>Water</span><span>Food</span><span>Amount</span></div>
    <div class="log-row"><span class="blank" style="width:46px"></span><span class="blank" style="width:64px"></span><span class="blank" style="width:74px"></span><span class="blank" style="width:58px"></span><span class="blank" style="width:74px"></span></div>
    <div class="log-row"><span class="blank" style="width:46px"></span><span class="blank" style="width:64px"></span><span class="blank" style="width:74px"></span><span class="blank" style="width:58px"></span><span class="blank" style="width:74px"></span></div>
    <div class="log-row"><span class="blank" style="width:46px"></span><span class="blank" style="width:64px"></span><span class="blank" style="width:74px"></span><span class="blank" style="width:58px"></span><span class="blank" style="width:74px"></span></div>
    <div class="log-row"><span class="blank" style="width:46px"></span><span class="blank" style="width:64px"></span><span class="blank" style="width:74px"></span><span class="blank" style="width:58px"></span><span class="blank" style="width:74px"></span></div>
  </section>

  <section class="col col-left" style="top:615px">
    <div class="label">Diapers</div>
    <div class="log-head" style="margin-top:12px"><span style="width:110px">Time</span><span>Wet</span><span>BM</span></div>
  </section>
  <section class="col col-right" style="top:615px">
    <div class="label">Mood</div>
    <div class="log-head" style="margin-top:12px"><span>Happy</span><span>Sad</span><span>Unsettled</span></div>
  </section>

  <div class="icon-row">
    <div class="icon" role="img" aria-label="Pink stroller illustration" style="width:62px;height:56px;background:var(--stroller-rose)"></div>
    <div class="icon" role="img" aria-label="Gold baby bath tub illustration" style="width:82px;height:44px;background:var(--tub-gold)"></div>
    <div class="icon" role="img" aria-label="Mint ABC blocks illustration" style="width:56px;height:58px;background:var(--blocks-mint)"></div>
    <div class="icon" role="img" aria-label="Brown baby bottle illustration" style="width:38px;height:52px;background:var(--bottle-brown)"></div>
    <div class="icon" role="img" aria-label="Green diaper illustration" style="width:52px;height:36px;background:var(--diaper-green)"></div>
  </div>

  <section class="col col-left" style="top:805px;width:900px">
    <div class="label supplies">Supplies Needed Soon</div>
    <div class="supply-list">
      <span class="bullet">Diapers</span><span>Milk/Formula</span><span>Wet Wipes</span>
      <span class="bullet">Diaper Cream</span><span>Cereal</span><span>Baby Food</span>
      <span class="bullet">Other:</span><span></span><span></span>
    </div>
  </section>

  <section class="col col-left" style="top:950px;width:1000px">
    <div class="label">Special Notes</div>
    <div style="margin-top:14px">
      <div class="note-line"></div>
      <div class="note-line"></div>
      <div class="note-line"></div>
      <div class="note-line"></div>
    </div>
  </section>
</body>
</html>
```